Quarry - Web Design Project

We are seeking to have our website redesigned. Our current webpage is rather dated looking www.quarry-results.com We will be utilizing similar content to explain our services as what is in the website now. We do not see it at a retail portal but rather a website for those inquiring about our services as a reference check so to speak.

We wish to have a look that is considered clean, fresh, contemporary and contains a business savvy vibe.

We prefer isolated white background and also wish to retain the integrity of our Logo and colour scheme.

We are looking for something that doesnt look like it was designed at home on sitemarlo. We are hoping to find something that looks like it would reside on a tablet.

Hello designers!

We apologize for our tardiness as we have been quite preoccupied. We will be extending our invites to the end of January!

Hello All,

Please review our offer once again for updated requirements.  We are hoping to accept a design by months end.

Quarry

Target Market(s)

Business to business clients and Large manufacturers

Industry/Entity Type

Retail

Requirements
Must have
• Existing Logo

There must be an area dedicated to an intro video that will be incorporated on our landing page.

We require design of the other pages as well not only the landing page.

```html
<!DOCTYPE html>
<html lang="en">
<head>
<meta charset="utf-8">
<title>Quarry Performance Group</title>
<link rel="stylesheet" href="https://fonts.googleapis.com/css2?family=Hind:wght@400;500;600&family=Great+Vibes&family=Open+Sans:wght@400;600&family=Arimo:wght@400;700&display=swap">
<style>
:root{
  --ink:#555559;
  --ink-dark:#1b1b1b;
  --red:#d7181d;
  --panel:#222222;
  --frame:#8f8f8f;
  --footer:#0b0b0b;
  --footer-line:#3a3a3a;
  --lime:#b9e33a;
  --light:#e8e8e8;
}
*{box-sizing:border-box;margin:0;padding:0}
html,body{width:1043px;height:1200px;overflow:hidden;background:#fff}
body{position:relative;font-family:'Hind',sans-serif;color:var(--ink)}
.abs{position:absolute}

.topbar{left:31px;top:31px;width:981px;height:61px;border-radius:31px;
  background:linear-gradient(#3a3a3a,#0c0c0c 55%,#1a1a1a)}
.brand{left:72px;top:15px;width:172px;height:85px;background:#fff;display:flex;align-items:center;justify-content:center;gap:8px}
.brand-dot{width:14px;height:14px;border-radius:50%;background:var(--red)}
.brand-name{font-family:'Hind',sans-serif;font-weight:500;font-size:44px;color:#5a5a5c;letter-spacing:-1px;line-height:1}
.nav{left:245px;top:31px;height:61px;display:flex;list-style:none}
.nav li{height:61px;display:flex;align-items:center;padding-left:20px;border-right:1px solid #444;
  font-family:'Hind',sans-serif;font-size:12.5px;letter-spacing:.3px;color:#f2f2f2;text-transform:uppercase;white-space:nowrap}
.nav .n-home{width:107px;padding-left:49px}
.nav .n-who{width:117px}
.nav .n-cross{width:153px}
.nav .n-perf{width:202px}
.nav .n-sustain{width:160px;border-right:none}
.nav .current span{border-bottom:2px solid var(--red);padding-bottom:2px}

.hero{left:31px;top:117px;width:981px;height:294px;border:1px solid var(--frame)}
.intro-video{left:56px;top:142px;width:568px;height:243px;
  background:linear-gradient(180deg,#d8dcdc 0%,#9aa3a3 30%,#4f5557 50%,#6e7272 75%,#8a8c8c 100%);
  display:flex;align-items:center;justify-content:center}
.play{width:64px;height:64px}
.hero-panel{left:624px;top:142px;width:363px;height:243px;background:var(--panel)}
.hero-box{left:648px;top:167px;width:315px;height:194px;border:1px solid var(--red)}
.hero-the{left:680px;top:178px;font-family:'Great Vibes',cursive;font-size:40px;color:#ddd}
.hero-right{left:703px;top:224px;font-family:'Hind',sans-serif;font-weight:600;font-size:36px;color:#fff;line-height:1}
.hero-sol{left:702px;top:258px;font-family:'Hind',sans-serif;font-size:55px;color:#fff;line-height:1.1}

.welcome{left:56px;top:449px;width:505px}
.welcome h1{font-weight:400;font-size:26px;color:#4a4a4e;margin-bottom:20px}
.welcome p{font-size:14.5px;line-height:20.5px;letter-spacing:.2px;margin-bottom:20px}
.more{font-family:'Arimo',sans-serif;font-weight:700;font-size:12px;color:var(--red)}
.welcome .more{display:block;margin-top:22px;font-size:13px}

.teaser{left:624px;width:340px;height:92px}
.teaser .thumb{position:absolute;left:0;top:0;width:82px;height:92px;border:1px solid #ccc;padding:4px;background:#fff}
.teaser .thumb div{width:100%;height:100%}
.teaser h2{position:absolute;left:93px;top:0;font-family:'Open Sans',sans-serif;font-weight:600;font-size:14px;color:var(--ink-dark)}
.teaser p{position:absolute;left:93px;top:26px;width:240px;height:32px;overflow:hidden;font-family:'Open Sans',sans-serif;font-size:12.5px;line-height:16px;color:#666}
.teaser .more{position:absolute;left:93px;top:66px;font-size:11px}

.footer{left:0;top:779px;width:1043px;height:421px;background:var(--footer);
  background-image:repeating-linear-gradient(0deg,#0b0b0b 0 2px,#151515 2px 4px)}
.fcol{top:812px;width:265px;font-family:'Arimo',sans-serif}
.fcol h3{font-weight:400;font-size:19px;color:var(--light);padding-bottom:6px;border-bottom:1px solid var(--footer-line)}
.fnav{list-style:none}
.fnav li{font-size:12.5px;color:var(--lime);height:32px;line-height:32px;padding-left:2px;border-bottom:1px solid var(--footer-line)}
.map{left:365px;top:865px;width:204px;height:130px;border:1px solid #8aa83a;border-radius:8px;padding:4px}
.map div{width:100%;height:100%;border-radius:6px;background:linear-gradient(135deg,#e9e6df,#d6d3cb)}
.maplink{left:366px;top:1004px;font-family:'Arimo',sans-serif;font-weight:700;font-size:12px;color:var(--lime)}
.contact dl{margin-top:6px}
.contact .row{padding:5px 2px 4px;border-bottom:1px solid var(--footer-line)}
.contact .row:last-child{border-bottom:none}
.contact dt{font-weight:700;font-size:12px;color:var(--lime);margin-bottom:3px}
.contact dd{font-family:'Hind',sans-serif;font-size:12.5px;line-height:17px;color:var(--light)}
</style>
</head>
<body>

<header>
  <div class="abs topbar"></div>
  <div class="abs brand"><span class="brand-dot"></span><span class="brand-name">Quarry</span></div>
  <ul class="abs nav">
    <li class="n-home current"><span>Home</span></li>
    <li class="n-who">Who we are</li>
    <li class="n-cross">Cross the Quarry</li>
    <li class="n-perf">Performance Solutions</li>
    <li class="n-sustain">Sustain Solutions</li>
  </ul>
</header>

<section>
  <div class="abs hero"></div>
  <div class="abs intro-video" role="img" aria-label="Intro video: poster frame of a coastal highway curving along a cliff by the sea">
    <svg class="play" viewBox="0 0 64 64" aria-hidden="true">
      <circle cx="32" cy="32" r="30" fill="rgba(0,0,0,.55)" stroke="#fff" stroke-width="2"/>
      <path d="M26 20 L46 32 L26 44 Z" fill="#fff"/>
    </svg>
  </div>
  <div class="abs hero-panel"></div>
  <div class="abs hero-box"></div>
  <div class="abs hero-the">The</div>
  <div class="abs hero-right">RIGHT</div>
  <div class="abs hero-sol">Solutions</div>
</section>

<main>
  <article class="abs welcome">
    <h1>Welcome to Quarry Performance Group</h1>
    <p>Quarry Performance Group Inc. is the leading provider of profit generating and people development solutions. With the hands-on experience of best practices, the state-of-the-art technology and in-depth information we help companies increase their efficiencies and profits. Frank, honest, committed, valuable and rewarding are words that customers use to describe the quality services provided by Quarry Performance Group.</p>
    <p>Learn more about us, or find the right solutions for your specific business.We will be delighted to help you achieve better business results.</p>
    <span class="more">Read more</span>
  </article>

  <div class="abs teaser" style="top:454px">
    <div class="thumb"><div role="img" aria-label="Green round button with a puzzle piece icon" style="background:radial-gradient(circle,#7fd83a 0 45%,#3a9a18 55%,#fff 62%)"></div></div>
    <h2>Title Two Goes Here</h2>
    <p>Vim no sanctus volumus tincidunt, has eu nostrud laoreet detracto, qualisque</p>
    <span class="more">Read more</span>
  </div>
  <div class="abs teaser" style="top:579px">
    <div class="thumb"><div role="img" aria-label="Illustration of red puzzle pieces" style="background:radial-gradient(circle at 45% 45%,#e23a2a 0 30%,#f3d6d0 50%,#fff 65%)"></div></div>
    <h2>Title Three Goes Here</h2>
    <p>Vim no sanctus volumus tincidunt, has eu nostrud laoreet detracto, qualisque</p>
    <span class="more">Read more</span>
  </div>
</main>

<footer>
  <div class="abs footer"></div>
  <div class="abs fcol" style="left:41px">
    <h3>Navigation</h3>
    <ul class="fnav">
      <li>HOME</li><li>WHO WE ARE</li><li>CROSS THE QUARRY</li><li>PERFORMANCE</li><li>SOLUTIONS</li><li>SUSTAIN SOLUTIONS</li>
    </ul>
  </div>
  <div class="abs fcol" style="left:363px;width:267px"><h3>How to find us</h3></div>
  <div class="abs map"><div role="img" aria-label="Street map showing the office location"></div></div>
  <div class="abs maplink">View Larger Map</div>
  <div class="abs fcol contact" style="left:688px">
    <h3>Contact Us</h3>
    <dl>
      <div class="row"><dt>Phone:</dt><dd>+1.888.555.0142</dd></div>
      <div class="row"><dt>Mobile:</dt><dd>+1.888.555.0142</dd></div>
      <div class="row"><dt>Address:</dt><dd>58 Alder Row S, Lakefield<br>ON K0L 2H0, Canada</dd></div>
      <div class="row"><dt>Email:</dt><dd style="font-size:14px">info@quarry-results.com</dd></div>
    </dl>
  </div>
</footer>

</body>
</html>
```